Calm and Clarity Health Flyer (new business startup)

One page...clear enough to be read if faxed. This mental health clinic treats depression/anxiety in kids and adults. It also treats opiate and alcohol addiction. It's in downtown Elmira, NY and the owner of the clinic is from Elmira NY, where it's located. This clinic does not take health insurance, so it charges a low rate of $75 a visit once they pay the $125 starting fee.

Target Market(s)

doctors offices, new patients

Industry/Entity Type

Doctor

Requirements
Must have
• see microsoft word document. pdf is printed on the company letterhead.
Nice to have
• a simplified map would be nice. if you can include the building it would be a plus. The same two fonts were used in the business cards and letter head (kennedy small caps boo*) and Refrigerator Delux.

```html
<!DOCTYPE html>
<html lang="en">
<head>
<meta charset="utf-8">
<title>Calm and Clarity Health – Flyer</title>
<link rel="stylesheet" href="https://fonts.googleapis.com/css2?family=Cinzel:wght@400&family=Nunito:wght@800;900&family=Oswald:wght@300;400&family=Open+Sans:wght@400;600;700&family=Montserrat:wght@700&display=swap">
<style>
  :root {
    --charcoal: #363636;
    --orange: #f0612f;
    --orange-text: #f26a35;
    --blue: #2ea3da;
    --ink: #111111;
    --white: #ffffff;
    --footer-ink: #2b2b2b;
    --map-light: #e9e8e5;
    --map-mid: #dcdbd8;
  }
  * { margin: 0; padding: 0; box-sizing: border-box; }
  html, body { width: 849px; height: 1200px; overflow: hidden; background: var(--white); }
  .flyer { position: relative; width: 849px; height: 1200px; background: var(--charcoal); font-family: "Open Sans", sans-serif; color: var(--white); }

  .header { position: absolute; left: 0; top: 0; width: 849px; height: 210px; background: var(--charcoal); }
  .brand { position: absolute; left: 58px; top: 30px; display: flex; align-items: center; gap: 12px; }
  .brand-dot { width: 46px; height: 46px; border-radius: 50%; background: var(--orange); }
  .brand-name { font-family: "Montserrat", sans-serif; font-weight: 700; font-size: 27px; letter-spacing: -0.3px; color: var(--orange-text); }
  .provider { position: absolute; right: 46px; top: 108px; font-family: "Cinzel", serif; font-weight: 400; font-size: 40px; color: var(--blue); letter-spacing: 1px; white-space: nowrap; }
  .credentials { position: absolute; right: 46px; top: 158px; font-family: "Oswald", sans-serif; font-weight: 300; font-size: 15px; color: var(--white); white-space: nowrap; }

  .services { position: absolute; left: 0; top: 210px; width: 523px; height: 640px; background: var(--orange); padding: 76px 0 0 60px; list-style: none; }
  .services li { position: relative; font-family: "Nunito", sans-serif; font-weight: 900; font-size: 42px; line-height: 1.12; color: var(--ink); padding-left: 34px; margin-bottom: 34px; }
  .services li::before { content: ""; position: absolute; left: 0; top: 15px; width: 20px; height: 20px; border-radius: 50%; background: var(--white); }
  .services li.wide { line-height: 1.2; }

  .building-photo { position: absolute; left: 523px; top: 210px; width: 326px; height: 302px; background: linear-gradient(180deg, #a9c2dc 0%, #9a6a55 30%, #7a4e3e 70%, #8a8a88 100%); }
  .location-map { position: absolute; left: 523px; top: 512px; width: 326px; height: 338px; background: linear-gradient(180deg, var(--map-light) 0%, var(--map-mid) 100%); }

  .details { position: absolute; left: 92px; top: 880px; }
  .hours { font-family: "Montserrat", sans-serif; font-weight: 700; font-size: 28px; line-height: 38px; color: var(--orange-text); }
  .fees { margin-top: 2px; font-size: 21px; line-height: 34px; }
  .fee { display: flex; width: 590px; }
  .fee .leader { flex: 1; border-bottom: 2px dotted rgba(255,255,255,.8); margin: 0 6px 9px; }

  .motto { position: absolute; left: 92px; top: 1043px; font-size: 22px; line-height: 30px; }
  .note { position: absolute; left: 92px; top: 1083px; font-size: 14.5px; font-weight: 700; line-height: 19px; }

  .footer { position: absolute; left: 0; top: 1135px; width: 849px; height: 65px; background: var(--orange); font-family: "Oswald", sans-serif; font-weight: 300; font-size: 15px; color: var(--footer-ink); line-height: 1.45; }
  .footer-left { position: absolute; left: 86px; top: 10px; }
  .footer-right { position: absolute; right: 50px; top: 10px; text-align: right; }
</style>
</head>
<body>
<main class="flyer">
  <header class="header">
    <div class="brand">
      <span class="brand-dot"></span>
      <span class="brand-name">CALM AND CLARITY HEALTH</span>
    </div>
    <h1 class="provider">DANIEL REYES, RPA,PLLC</h1>
    <p class="credentials">(555) 014-2210 - Psychiatric Physician Assistant (PA-C-PSY, CAQ) dreyes.clinic@example.com</p>
  </header>

  <ul class="services">
    <li>Depression</li>
    <li>PTSD</li>
    <li>Addiction</li>
    <li>Anxiety</li>
    <li>ADHD</li>
    <li class="wide">Bipolar Childhood Mood Disorders</li>
  </ul>

  <div class="building-photo" role="img" aria-label="Photo of the downtown brick clinic building on a street corner"></div>
  <div class="location-map" role="img" aria-label="Street map of downtown Elmira marking the clinic location"></div>

  <section class="details">
    <h2 class="hours">Hours: Monday and Saturdays 9-4pm</h2>
    <div class="fees">
      <div class="fee"><span>Psychiatric Evaluation (45min)</span><span class="leader"></span><span>$125*</span></div>
      <div class="fee"><span>Psychiatric Office Visit (15min)</span><span class="leader"></span><span>$75*</span></div>
      <div>Ages:&nbsp; 6 years old and up</div>
    </div>
  </section>

  <p class="motto">“We work for you, not the insurance companies”</p>
  <p class="note">*Although we do not partner with any Health Insurance Companies at this time,<br>a bill will be provided to you at the time of service for you to submit to your insurance company.</p>

  <footer class="footer">
    <div class="footer-left">210 W. Water St #3 Elmira, NY 14901<br>With Dr. Helen Marsh</div>
    <div class="footer-right">(P) 555-014-2210 (F) 555-014-7734<br>www.calm-clarity.com</div>
  </footer>
</main>
</body>
</html>
```